Harborne Cellarbook: the premier wine registry - (need business cards)

We have a logo designed, and now we need business cards for our 3 founders. Harborne Cellarbook is the premier wine registry for weddings. I am envisioning the wine glass with the heart in it as our signature symbol. (FYI- on the red background file, only use the part that has the red background; the brown colors are not relevant)

```html
<!DOCTYPE html>
<html lang="en">
<head>
<meta charset="utf-8">
<title>Harborne Cellarbook – Business Card</title>
<link rel="stylesheet" href="https://fonts.googleapis.com/css2?family=Roboto:wght@400;500&display=swap">
<style>
  :root {
    --page-bg: #e9e5e1;
    --card-frost: #d8d2ce;
    --burgundy-light: #80304c;
    --burgundy-mid: #6a2139;
    --burgundy-deep: #4e1023;
    --heart-fill: #5a1428;
    --heart-edge: #e8d9d4;
    --text-light: #f1e6ea;
    --text-soft: #e3cfd6;
    --brand-tone: #dcc5b8;
  }
  * { margin: 0; padding: 0; box-sizing: border-box; }
  html, body {
    width: 1200px; height: 969px; overflow: hidden;
    background: var(--page-bg);
    font-family: "Roboto", Arial, sans-serif;
  }
  .business-card {
    position: absolute; left: 100px; top: 200px;
    width: 1000px; height: 568px; overflow: hidden;
    background: var(--card-frost);
    box-shadow: 0 10px 30px rgba(60, 30, 40, 0.18);
  }
  .card-art { position: absolute; inset: 0; }
  .holder-name {
    position: absolute; left: 66px; top: 72px;
    font-size: 33px; font-weight: 500; color: var(--text-light);
  }
  .holder-title {
    position: absolute; left: 66px; top: 116px;
    font-size: 24px; font-weight: 400; color: var(--text-soft);
  }
  .postal-address {
    position: absolute; left: 66px; top: 262px;
    font-size: 22px; line-height: 31px; color: var(--text-soft); font-style: normal;
  }
  .contact-list {
    position: absolute; left: 66px; top: 336px; list-style: none;
  }
  .contact-list li {
    display: flex; align-items: center; height: 32px;
    font-size: 21.5px; color: var(--text-soft);
  }
  .contact-list svg { width: 22px; height: 22px; margin-right: 16px; fill: var(--text-soft); }
  .brand-name {
    position: absolute; left: 480px; top: 262px; width: 410px;
    text-align: center; font-size: 34px; font-weight: 400;
    letter-spacing: 1px; color: var(--brand-tone);
  }
</style>
</head>
<body>
  <section class="business-card">
    <svg class="card-art" viewBox="0 0 1000 568" width="1000" height="568" aria-hidden="true">
      <defs>
        <linearGradient id="panelGradient" x1="0" y1="0" x2="1" y2="0.4">
          <stop offset="0" stop-color="var(--burgundy-light)"/>
          <stop offset="0.55" stop-color="var(--burgundy-mid)"/>
          <stop offset="1" stop-color="var(--burgundy-deep)"/>
        </linearGradient>
      </defs>
      <path class="burgundy-panel" d="M0 0 H690 L690 568 H0 Z" fill="url(#panelGradient)"/>
      <path class="heart-shape"
        d="M683 566 C600 470 372 330 372 190 C372 60 470 -10 560 -5 C620 0 665 30 683 50 C705 25 760 -5 820 -5 C920 0 995 80 992 200 C988 340 760 470 683 566 Z"
        fill="var(--heart-fill)" stroke="var(--heart-edge)" stroke-width="2"/>
    </svg>

    <h1 class="holder-name">Daniel Hartwell</h1>
    <p class="holder-title">President</p>

    <address class="postal-address">2141 Larkspur Court<br>Juneau, Alaska 34512</address>

    <ul class="contact-list">
      <li><svg viewBox="0 0 24 24"><path d="M6.6 10.8a15 15 0 0 0 6.6 6.6l2.2-2.2a1 1 0 0 1 1-.25 11.4 11.4 0 0 0 3.6.6 1 1 0 0 1 1 1V20a1 1 0 0 1-1 1A17 17 0 0 1 3 4a1 1 0 0 1 1-1h3.5a1 1 0 0 1 1 1c0 1.25.2 2.45.6 3.6a1 1 0 0 1-.25 1z"/></svg>369-480-2713</li>
      <li><svg viewBox="0 0 24 24"><path d="M7 1h10a2 2 0 0 1 2 2v18a2 2 0 0 1-2 2H7a2 2 0 0 1-2-2V3a2 2 0 0 1 2-2zm0 3v14h10V4zm5 15.5a1 1 0 1 0 0 2 1 1 0 0 0 0-2z"/></svg>369-604-1928</li>
      <li><svg viewBox="0 0 24 24"><path d="M7 3h10v5H7zM3 9h18v8h-3v-3H6v3H3zm4 6h10v6H7z"/></svg>369-735-4406</li>
      <li><svg viewBox="0 0 24 24"><path d="M3 6h18v12H3zm2 2v.5l7 4.5 7-4.5V8l-7 4.5z"/></svg>info@harbornecellarbook.com</li>
      <li><svg viewBox="0 0 24 24"><path d="M12 2a10 10 0 1 0 0 20 10 10 0 0 0 0-20zm-1 17.9A8 8 0 0 1 4.1 10l4.9 4.9v1a2 2 0 0 0 2 2zm6.9-2.5A2 2 0 0 0 16 16h-1v-3a1 1 0 0 0-1-1H8v-2h2a1 1 0 0 0 1-1V7h2a2 2 0 0 0 2-2v-.4a8 8 0 0 1 2.9 12.8z"/></svg>www.harbornecellarbook.com</li>
    </ul>

    <p class="brand-name">Harborne Cellarbook</p>
  </section>
</body>
</html>
```